Philadelphia-based Nonprofit Needs Invitation Design for 11th Annual Cook-Off Fundraiser

Venture Guild (VG) is a non-profit 501(c)(3) microenterprise development organization focused on growing businesses and jobs in our local communities. By connecting hundreds of entrepreneurs each year with access to capital, one-on-one technical assistance, business training and networking opportunities, Venture Guild helps promising individuals to develop economic self-sufficiency and create job opportunities through business ownership.

The theme for our 11th annual Plate of Promise cook-off fundraiser, “Tastes from Around the World: Savor the Flavors,” reflects our commitment to fostering and celebrating the diverse network of entrepreneurs, business owners, and supporters that make VG’s work possible.

Plate of Promise is a chance for Venture Guild to showcase the culinary talents of our entrepreneurs and business owners, while also hosting a fun-filled night with celebrity guest judges, delicious hors d'oeuvres and desserts, a silent auction, and an exciting cook-off contest.

We would like a double-sided, two-color folded invitation (fold size: 5" x 7"); a double-sided, two-color reply card (5” x 4”); a mailing envelope (A7 envelope, grayscale) and a reply envelope (A2 envelope, grayscale). For an example of the design that was on the cover of last year's invitation, see here: http://www.myventureguild.example/sites/vg.relaybureau.example/files/imagecache/250px_thumb/signature_images/VG_HearthsideWarmth.png.

The final design should appeal to a broad range of potential attendees and be inviting and warm. While we send out a different invitation for each Plate of Promise fundraiser, we were very pleased with last year’s invitation (attached, “Plate of Promise Invitation_2011”) and would like an invitation design that is similar (for color scheme please refer to the web link in the above paragraph). A scanned copy of the reply card is also attached ("Plate of Promise Reply Cards 2011"). Finally a copy of the outer envelope is attached ("Plate of Promise Outer Envelope_2011").

Target Market(s)

Our target market includes: existing and past donors; local business owners; and entrepreneurs.

Industry/Entity Type

Non-Profit

Requirements
Must have
• - The main illustration on the invitation should be food-themed
- The invitation should include all of the copy in the attached word .doc ("Plate of Promise Invitation Copy_2013").
Should not have
• - Any designs, backgrounds or fonts that make the invitation difficult to read or understand

```html
<!DOCTYPE html>
<html lang="en">
<head>
<meta charset="utf-8">
<title>Plate of Promise Invitation – Inside Panels</title>
<link rel="stylesheet" href="https://fonts.googleapis.com/css2?family=Open+Sans:wght@400;600&family=Tinos:wght@400;700&family=Marcellus&family=Encode+Sans+Condensed:wght@400;500&display=swap">
<style>
  :root {
    --page: #ecebe8;
    --paper: #ffffff;
    --guild-blue: #6474ac;
    --guild-red: #b3262a;
    --ink: #1f1f1f;
    --ink-soft: #2a3050;
    --white: #ffffff;
  }
  * { margin: 0; padding: 0; box-sizing: border-box; }
  html, body { width: 1200px; height: 1000px; overflow: hidden; background: var(--page); }
  .invitation {
    position: absolute; left: 80px; top: 137px; width: 1040px; height: 726px;
    display: flex; box-shadow: 0 4px 14px rgba(0,0,0,.18);
  }
  .panel { position: relative; width: 520px; height: 100%; }
  .panel--left { background: var(--paper); }
  .panel--right { background: var(--guild-blue); }
  .panel-band { position: absolute; left: 0; top: 38px; width: 100%; height: 25px; background: var(--guild-blue); }

  .judges { position: absolute; top: 92px; width: 100%; text-align: center; }
  .judges-kicker { font-family: "Open Sans", sans-serif; color: var(--guild-red); font-size: 28px; line-height: 28px; letter-spacing: -0.5px; }
  .judges-title { font-family: "Tinos", serif; font-weight: 400; color: var(--guild-blue); font-size: 31px; line-height: 32px; letter-spacing: -0.3px; }
  .judge-list { list-style: none; margin-top: 8px; }
  .judge { font-family: "Encode Sans Condensed", sans-serif; font-size: 16px; line-height: 29px; color: var(--ink); letter-spacing: -0.4px; }
  .judge-name { font-family: "Marcellus", serif; font-size: 21px; letter-spacing: -0.3px; }

  .program { position: absolute; top: 297px; width: 100%; list-style: none; text-align: center; }
  .program li { font-family: "Tinos", serif; color: var(--guild-red); font-size: 24px; line-height: 52px; }

  .theme-copy {
    position: absolute; left: 40px; top: 121px; width: 440px; text-align: center;
    font-family: "Encode Sans Condensed", sans-serif; font-size: 12px; line-height: 29px; color: var(--ink-soft);
  }

  .event-date { position: absolute; left: 0; top: 0; width: 100%; height: 100%; }
  .date-month {
    position: absolute; left: 110px; top: 382px;
    font-family: "Tinos", serif; font-weight: 700; color: var(--white);
    font-size: 165px; line-height: 1; letter-spacing: -4px;
    transform: scaleX(0.85); transform-origin: left top;
  }
  .date-day { position: absolute; left: 190px; top: 403px; font-family: "Open Sans", sans-serif; color: var(--guild-red); font-size: 29px; line-height: 1; letter-spacing: -1px; }
  .date-number { position: absolute; left: 133px; top: 510px; font-family: "Tinos", serif; color: var(--ink); font-size: 95px; line-height: 1; letter-spacing: -7px; }
  .date-time { position: absolute; left: 268px; top: 545px; font-family: "Encode Sans Condensed", sans-serif; font-weight: 500; color: var(--ink); font-size: 19px; line-height: 1; letter-spacing: -0.8px; }

  .venue { position: absolute; top: 614px; width: 100%; text-align: center; }
  .venue-name { font-family: "Open Sans", sans-serif; color: var(--guild-red); font-size: 30px; line-height: 36px; letter-spacing: -1px; }
  .venue-address { font-family: "Encode Sans Condensed", sans-serif; font-weight: 500; color: var(--ink); font-size: 17px; line-height: 22px; }
  .web-link { position: absolute; top: 700px; width: 100%; text-align: center; font-family: "Tinos", serif; color: var(--white); font-size: 14px; }
  .web-link strong { font-size: 15px; }
</style>
</head>
<body>
<main class="invitation">
  <section class="panel panel--left">
    <div class="panel-band"></div>
    <div class="judges">
      <p class="judges-kicker">Featuring</p>
      <h2 class="judges-title">Special Guest Judges</h2>
      <ul class="judge-list">
        <li class="judge"><span class="judge-name">Rosa Delmont</span>, Co-owner, Rosa’s Corner Bistro Fairmount</li>
        <li class="judge"><span class="judge-name">Daniel Marsh</span>, Executive chef and co-owner, Casa Soleado</li>
        <li class="judge"><span class="judge-name">Owen Calder</span>, Owner, Calder’s Smokehouse</li>
      </ul>
    </div>
    <ul class="program">
      <li>Entertainment Includes</li>
      <li>Cook-off Contest</li>
      <li>Silent Auction</li>
      <li>Hors d’oeuvres</li>
      <li>Open Bar</li>
      <li>The People’s Choice Award</li>
    </ul>
  </section>

  <section class="panel panel--right">
    <p class="theme-copy">This year’s theme, “Tastes from Around the World: Savor the Flavors,” reflects our commitment to fostering and celebrating the diverse network of entrepreneurs, business owners, and supporters that make our work possible. The festivities will include our signature bake-off and cook-off competitions, where our innovative entrepreneurs compete for top prizes. Special guest judges—including Rosa Delmont, co-owner of Rosa’s Corner Bistro Fairmount, Daniel Marsh, executive chef and co-owner of Casa Soleado, and Owen Calder, owner of Calder’s Smokehouse—will determine the winners. Don’t forget to bring your appetite to sample each contestant’s dish and vote for People’s Choice Award!</p>

    <div class="event-date">
      <span class="date-month">April</span>
      <span class="date-day">MONDAY</span>
      <span class="date-number">29</span>
      <span class="date-time">6:00 p.m. – 8:00 p.m.</span>
    </div>

    <div class="venue">
      <p class="venue-name">Riverside Hall Philadelphia</p>
      <p class="venue-address">1200 Harbor Lane, Philadelphia, PA 19000</p>
    </div>
    <p class="web-link">Visit us online at <strong>MyVentureGuild.example</strong></p>
  </section>
</main>
</body>
</html>
```